Walk Bright through the Seasons: 52 Weeks to a Year of Courage and Calm

This is a non-fiction, self-help book. The first edition was published a decade ago, and it needs a new design. Nothing too literal (no actual hearts on the cover) but something inspirational or perhaps something quite plain. The current cover is below for reference, but I DO NOT want something similar to that. It is outdated.

The cover must include:

1. Title: Walk Bright through the Seasons
2. Subtitle: 52 Weeks to a Year of Courage and Calm
3. Author Name: Tobin Wells

It should also have plenty of "white space" in other words the fonts shouldnt be so big that they take up the whole cover.

Dimensions: 9" x 6.25"

Target Market(s)

adults interested in personal development

Font styles to use
Serif
Script

Colors

Designer to choose colors to be used in the design.

Requirements
Must have
• Classic look and feel. The current design is too busy. I have included examples of the style I like below. I'm open to a singular graphic/photo but nothing more than that. Probably plain text is best.
• Please look at the samples I have included of best-selling books in the genre that I like. The cover should be modeled after these.

```html
<!DOCTYPE html>
<html lang="en">
<head>
<meta charset="utf-8">
<title>Walk Bright through the Seasons — Tobin Wells</title>
<link rel="stylesheet" href="https://fonts.googleapis.com/css2?family=Cinzel:wght@400;500&family=Crimson+Pro:ital,wght@0,400;1,400&display=swap">
<style>
  :root {
    --backdrop: #e4e7e9;
    --cover: #ffffff;
    --title-blue: #1f7cc4;
    --band-blue: #2282c9;
    --ink: #111111;
    --quote-ink: #222222;
    --white: #ffffff;
    --metal-light: #f4f5f6;
    --metal-mid: #c9ccd0;
    --metal-dark: #5d6166;
  }
  * { margin: 0; padding: 0; box-sizing: border-box; }
  html, body {
    width: 1200px; height: 800px; overflow: hidden;
    background: var(--backdrop);
  }
  .book-cover {
    position: absolute; left: 350px; top: 40px;
    width: 500px; height: 720px;
    background: var(--cover);
    overflow: hidden;
  }
  .title-main {
    position: absolute; left: 0; width: 100%;
    text-align: center;
    font-family: "Cinzel", "Times New Roman", serif;
    font-weight: 500;
    color: var(--title-blue);
    line-height: 1;
  }
  .title-line-one { top: 58px; font-size: 50px; letter-spacing: 0.5px; }
  .title-line-three { top: 168px; font-size: 74px; letter-spacing: 1px; }
  .title-connector {
    position: absolute; left: 48px; right: 48px; top: 118px;
    display: flex; align-items: center; gap: 14px;
    font-family: "Crimson Pro", Georgia, serif;
    font-style: italic;
    font-size: 46px;
    color: var(--ink);
    line-height: 1;
  }
  .title-connector .rule {
    flex: 1; height: 2px; background: var(--ink);
  }
  .subtitle {
    position: absolute; left: 0; width: 100%; top: 280px;
    text-align: center;
    font-family: "Crimson Pro", Georgia, serif;
    font-style: italic;
    font-size: 38px;
    line-height: 46px;
    color: var(--ink);
  }
  .compass-art {
    position: absolute; left: 0; top: 380px;
    width: 330px; height: 224px;
  }
  .endorsement {
    position: absolute; right: 55px; top: 452px;
    width: 160px;
    text-align: right;
    font-family: "Crimson Pro", Georgia, serif;
    font-size: 15px;
    line-height: 19px;
    color: var(--quote-ink);
  }
  .endorsement-source {
    margin-top: 6px;
    letter-spacing: 0.5px;
  }
  .author-band {
    position: absolute; left: 0; bottom: 0;
    width: 100%; height: 116px;
    background: var(--band-blue);
    display: flex; align-items: center; justify-content: center;
  }
  .author-name {
    font-family: "Cinzel", "Times New Roman", serif;
    font-weight: 400;
    font-size: 36px;
    letter-spacing: 1px;
    color: var(--white);
  }
</style>
</head>
<body>
  <main class="book-cover">
    <h1 class="book-title">
      <span class="title-main title-line-one">WALK BRIGHT</span>
      <span class="title-connector"><span class="rule"></span>through the<span class="rule"></span></span>
      <span class="title-main title-line-three">SEASONS</span>
    </h1>

    <p class="subtitle">52 Weeks to a Year of<br>Courage and Calm</p>

    <svg class="compass-art" viewBox="0 0 330 224" role="img" aria-label="Photograph of a silver compass seen from above, its needle pointing north-east">
      <defs>
        <radialGradient id="compassFace" cx="0.24" cy="0.98" r="0.75">
          <stop offset="0" stop-color="var(--metal-light)"/>
          <stop offset="0.7" stop-color="var(--metal-mid)"/>
          <stop offset="1" stop-color="var(--metal-dark)"/>
        </radialGradient>
      </defs>
      <circle cx="78" cy="222" r="228" fill="url(#compassFace)"/>
    </svg>

    <blockquote class="endorsement">
      <p>“Lorem ipsum dolor sit amet, consectetur adipisicing elit”.</p>
      <p class="endorsement-source">EIUSMOD<br>TEMPOR.</p>
    </blockquote>

    <footer class="author-band">
      <span class="author-name">TOBIN WELLS</span>
    </footer>
  </main>
</body>
</html>
```